Professional Law Firm Rebranding Brochure Layout Design

Our law firm is changing its name from The Law Office of Dana Moreno, PLLC to MORENO.LAW. I would like a 4-page color brochure (cover, page 2, page 3, back) that announces and explains our rebranding. I have attached lots of files that should be helpful. I envision the words "The Law Office of Dana Moreno, PLLC is now known as MORENO.LAW" at the top of the front cover. Feel free to review our website at https://moreno-legal.example to get an idea of the look and feel we like. Tall buildings and other professional images work well.

Target Market(s)

Businesses, law firm clients, entrepreneurs, startups, corporations

Industry/Entity Type

Legal

Font styles to use
Sans Serif

Colors
cfdeed
85abd2
3276b5
0555a3
cee9f5
85cae6
33a6d7
0492cd

Requirements
Must have
• Professional appearance, photos & bios of team members, explanation of rebranding - finished product is US letter size

```html
<!DOCTYPE html>
<html lang="en">
<head>
<meta charset="utf-8">
<title>MORENO.LAW – Name Change Brochure Spread</title>
<link href="https://fonts.googleapis.com/css2?family=Montserrat:wght@500;600;700;800&family=Open+Sans:wght@400;600&display=swap" rel="stylesheet">
<style>
  :root{
    --navy:#0f2350;
    --ink:#23324a;
    --muted:#5c6b80;
    --blue-deep:#0555a3;
    --blue:#3276b5;
    --blue-bright:#0492cd;
    --blue-mid:#33a6d7;
    --blue-soft:#85cae6;
    --blue-pale:#cee9f5;
    --steel:#85abd2;
    --mist:#cfdeed;
    --slate:#3d4d5e;
    --paper:#ffffff;
    --chart-red:#d63a3a;
  }
  *{box-sizing:border-box;margin:0;padding:0}
  html,body{width:1200px;height:840px;overflow:hidden}
  body{background:var(--navy);font-family:"Open Sans",Arial,sans-serif;color:var(--ink);position:relative}

  .spread{position:absolute;left:40px;top:58px;width:1120px;height:724px;display:flex;box-shadow:0 14px 40px rgba(0,0,0,.45)}
  .page{position:relative;width:560px;height:724px;background:var(--paper);overflow:hidden}
  .page--left{border-right:1px solid #d9dfe7}
  .page--left::before{content:"";position:absolute;left:0;top:0;width:100%;height:8px;background:var(--blue-deep)}

  /* ---------- left page ---------- */
  .feature-title{position:absolute;top:28px;width:100%;text-align:center;font-family:"Montserrat",sans-serif;font-weight:800;font-size:22px;letter-spacing:.5px;color:var(--blue-deep)}
  .feature-intro{position:absolute;top:60px;left:60px;right:60px;text-align:center;font-size:8px;line-height:1.45;color:var(--muted)}

  .reason{position:absolute;color:#fff;padding:12px 18px}
  .reason h3{font-family:"Montserrat",sans-serif;font-weight:700;font-size:11.5px;letter-spacing:.3px;margin-bottom:5px;text-align:center}
  .reason p{font-size:7.5px;line-height:1.5;opacity:.95}
  .reason--1{left:0;top:92px;width:320px;height:86px;background:var(--blue-deep);clip-path:polygon(0 0,92% 0,100% 50%,92% 100%,0 100%)}
  .reason--2{left:258px;top:188px;width:302px;height:82px;background:var(--blue-bright);clip-path:polygon(8% 0,100% 0,100% 100%,8% 100%,0 50%)}
  .reason--3{left:0;top:280px;width:300px;height:80px;background:var(--blue-mid);clip-path:polygon(0 0,92% 0,100% 50%,92% 100%,0 100%)}
  .reason--4{left:0;top:370px;width:440px;height:78px;background:linear-gradient(90deg,var(--blue-deep),var(--blue));clip-path:polygon(0 0,94% 0,100% 50%,94% 100%,0 100%)}
  .reason--5{left:232px;top:458px;width:328px;height:80px;background:var(--blue);clip-path:polygon(8% 0,100% 0,100% 100%,8% 100%,0 50%)}
  .reason--6{left:150px;top:560px;width:330px;height:86px;background:var(--blue-bright)}
  .reason--4 h3,.reason--3 h3,.reason--1 h3{text-align:left}
  .reason--3 p{padding-right:24px}

  .photo--handshake{position:absolute;left:300px;top:92px;width:260px;height:86px;background:linear-gradient(120deg,#a9c3dc,#3d6fa3 60%,#1d3f6b)}

  .search-panel{position:absolute;left:30px;top:188px;width:220px;height:82px;font-size:6.5px;color:var(--muted)}
  .search-panel .engine{display:flex;align-items:center;gap:4px;font-weight:600;color:var(--ink);margin-bottom:5px}
  .search-panel .engine i,.result i{display:inline-block;width:9px;height:9px;background:var(--mist);border:1px solid var(--steel)}
  .result{display:flex;gap:6px;margin-bottom:5px}
  .result i{width:20px;height:20px;flex:none;border-radius:2px}
  .result b{display:block;color:var(--blue-deep);font-weight:600;font-size:7px}

  .brand-names{position:absolute;left:320px;top:292px;width:220px;text-align:center}
  .brand-name{font-family:"Open Sans",sans-serif;font-weight:600;font-size:16px;color:var(--ink);line-height:1.3}
  .brand-name + .brand-name{margin-top:8px}

  .chart{position:absolute;left:36px;top:456px;width:186px;height:96px;border:1px solid var(--mist);background:#fff;padding:5px}
  .chart h4{font-family:"Montserrat",sans-serif;font-size:6px;font-weight:600;color:var(--blue-deep);margin-bottom:3px}

  .skyline-band{position:absolute;left:0;bottom:0;width:100%;height:70px;background:linear-gradient(180deg,var(--blue-pale),var(--blue-soft))}

  /* ---------- right page ---------- */
  .team-top{position:absolute;left:0;top:0;width:100%;height:6px;background:var(--blue-bright)}
  .team-header{position:absolute;left:0;top:24px;width:100%;height:128px;background:linear-gradient(90deg,var(--slate),#6c7d8c)}
  .team-header h2{position:absolute;left:40px;top:24px;font-family:"Montserrat",sans-serif;font-weight:700;font-size:22px;color:#fff;letter-spacing:.5px}
  .team-header p{position:absolute;left:40px;top:58px;width:400px;font-size:13px;line-height:1.35;color:#eef3f8;font-style:italic}

  .member{position:absolute;width:160px;text-align:center}
  .member .portrait{width:110px;height:108px;margin:0 auto 6px;border:4px solid var(--blue-bright);border-radius:12px;background:linear-gradient(160deg,var(--mist),var(--steel))}
  .member h3{font-family:"Montserrat",sans-serif;font-weight:700;font-size:10px;color:var(--blue-bright);letter-spacing:.3px;text-transform:uppercase}
  .member .role{font-family:"Montserrat",sans-serif;font-size:6.5px;font-weight:600;color:var(--muted);text-transform:uppercase;margin-bottom:4px}
  .member .bio{font-size:6.5px;line-height:1.5;color:var(--muted)}
  .member--1{left:30px;top:186px}
  .member--2{left:200px;top:236px}
  .member--3{left:370px;top:276px}
  .member--4{left:30px;top:430px}
  .member--5{left:200px;top:470px}
  .member--6{left:370px;top:520px}
</style>
</head>
<body>
<main class="spread">

  <section class="page page--left">
    <h1 class="feature-title">LAW FIRM NAME CHANGE</h1>
    <p class="feature-intro">Our firm has a new name. The Law Office of Dana Moreno, PLLC is now MORENO.LAW. Here are six reasons we made this change for our clients.</p>

    <div class="reason reason--1">
      <h3>1. IT'S SHORTER.</h3>
      <p>A shorter name is easier to remember, easier to type and easier to share with others.</p>
    </div>
    <div class="photo--handshake" role="img" aria-label="Photo of a business handshake in front of city towers"></div>

    <div class="search-panel">
      <div class="engine"><i></i>Search</div>
      <div class="result"><i></i><div><b>The Law Office of Dana Moreno, PLLC</b>Business law for startups and growing companies.</div></div>
      <div class="result"><i></i><div><b>moreno-legal.example</b>Contracts, formation and counsel.</div></div>
    </div>
    <div class="reason reason--2">
      <h3>2. IT'S DISTINCTIVE.</h3>
      <p>No other firm uses this name, so clients can find and recognize us at once.</p>
    </div>

    <div class="reason reason--3">
      <h3>3. IT TELLS PEOPLE HOW TO FIND US.</h3>
      <p>Our name is also our web address, pointing people straight to our website.</p>
    </div>
    <div class="brand-names">
      <div class="brand-name">marketly.com</div>
      <div class="brand-name">legaldesk online</div>
    </div>

    <div class="reason reason--4">
      <h3>4. IT'S SUGGESTIVE OF OUR BUSINESS.</h3>
      <p>The .law ending tells everyone right away that we are a law firm.</p>
    </div>

    <figure class="chart">
      <h4>VC company valuations ( over 12 years )</h4>
      <svg width="174" height="74" viewBox="0 0 174 74" aria-label="Area chart of valuations over twelve years">
        <g stroke="#e3e9f0" stroke-width=".6">
          <line x1="12" y1="8" x2="172" y2="8"/><line x1="12" y1="24" x2="172" y2="24"/>
          <line x1="12" y1="40" x2="172" y2="40"/><line x1="12" y1="56" x2="172" y2="56"/>
        </g>
        <polygon fill="var(--chart-red)" points="12,64 12,20 26,18 40,22 54,16 68,19 82,14 96,17 110,12 124,15 138,11 152,16 166,13 172,14 172,64"/>
        <line x1="12" y1="64" x2="172" y2="64" stroke="#9aa7b6" stroke-width=".8"/>
        <line x1="12" y1="4" x2="12" y2="64" stroke="#9aa7b6" stroke-width=".8"/>
      </svg>
    </figure>
    <div class="reason reason--5">
      <h3>5. IT'S APPEALING TO OUR CLIENTS.</h3>
      <p>Clients prefer modern, simple names that reflect a forward-looking legal practice.</p>
    </div>

    <div class="reason reason--6">
      <h3>6. IT'S INCLUSIVE.</h3>
      <p>Our new name welcomes every member of the team, not just the founder.</p>
    </div>

    <div class="skyline-band" role="img" aria-label="Soft city skyline backdrop"></div>
  </section>

  <section class="page page--right">
    <div class="team-top"></div>
    <header class="team-header" role="img" aria-label="Office interior photo behind heading">
      <h2>OUR TEAM</h2>
      <p>Our team is committed to being responsive and providing clients with direct and personal attention.</p>
    </header>

    <article class="member member--1">
      <div class="portrait" role="img" aria-label="Portrait of Nadia Farrow"></div>
      <h3>Nadia Farrow</h3>
      <div class="role">Legal Assistant &amp; Communications Manager</div>
      <p class="bio">Nadia keeps our clients informed, manages firm communications and supports attorneys on every matter with care and precision.</p>
    </article>
    <article class="member member--2">
      <div class="portrait" role="img" aria-label="Portrait of Theo Brandt"></div>
      <h3>Theo Brandt</h3>
      <div class="role">Attorney</div>
      <p class="bio">Theo advises startups on formation, financing and contracts, helping founders build strong legal foundations for lasting growth.</p>
    </article>
    <article class="member member--3">
      <div class="portrait" role="img" aria-label="Portrait of Dana Moreno"></div>
      <h3>Dana Moreno</h3>
      <div class="role">Attorney / Founder</div>
      <p class="bio">Dana founded the firm to give businesses practical, direct counsel and leads our corporate and transactional practice today.</p>
    </article>
    <article class="member member--4">
      <div class="portrait" role="img" aria-label="Portrait of Laura Whitfield"></div>
      <h3>Laura Whitfield</h3>
      <div class="role">Managing Partner</div>
      <p class="bio">Laura oversees firm operations and client service, making sure every engagement runs smoothly from first call to close.</p>
    </article>
    <article class="member member--5">
      <div class="portrait" role="img" aria-label="Portrait of Jenna Hale"></div>
      <h3>Jenna Hale</h3>
      <div class="role">Paralegal</div>
      <p class="bio">Jenna prepares filings, tracks deadlines and organizes documents so our attorneys can focus on solving client problems.</p>
    </article>
    <article class="member member--6">
      <div class="portrait" role="img" aria-label="Portrait of Mira Castell"></div>
      <h3>Mira Castell</h3>
      <div class="role">Attorney</div>
      <p class="bio">Mira handles commercial agreements and employment matters, guiding growing companies through negotiations with clear, steady advice.</p>
    </article>
  </section>

</main>
</body>
</html>
```